Speech Pathology card for parents of young children

I need a professional, yet fun card for my speech and language pathology services.
I'm trying to offer my speech therapy services to parents of young children. These parents will most likely be women. I want the card to have a fun feel to it and have a concept of speech and language in it (kind of like the cartoon I've attached below showing a boy/girl talking).

I'd want a white background on the card and to bring in some bright colors as well.

Please include the KROV logo in a smaller size on a free corner of the card.

Target Market(s)

parents of young children

Contact Information for Business Card

must have my information and I'd like it to have the KROV logo (small) somewhere in the corner)

Font styles to use
Serif
Sans Serif

Colors

Designer to choose colors to be used in the design.

Requirements
Must have
• The card title should read: Speech-Language Pathologist
• Rosalind Pettry
• MS CCC-SLP/TSSLD (this under the name)
• 415 906 2283
• rosiepettry@kelvormail.net
Nice to have
• i'm looking for a card with a white background and a fun icon that encompasses speaking... similar to the one I've attached.

```html
<!DOCTYPE html>
<html lang="en">
<head>
<meta charset="utf-8">
<title>Speech-Language Pathologist – Business Card</title>
<link rel="stylesheet" href="https://fonts.googleapis.com/css2?family=Archivo+Black&family=Montserrat:wght@400;600;700&display=swap">
<style>
  :root {
    --backdrop: #ece8e2;
    --card: #ffffff;
    --band: #f04e23;
    --band-text: #ffffff;
    --name: #8e2a8f;
    --email: #e2127a;
    --ink: #4a4a4a;
    --icon: #f05a28;
    --mark: #1d1d1d;
    --art-a: #dfe9f3;
    --art-b: #fbe3d6;
  }
  * { box-sizing: border-box; margin: 0; padding: 0; }
  html, body {
    width: 900px; height: 1200px; overflow: hidden;
    background: var(--backdrop);
  }
  .business-card {
    position: absolute; left: 84px; top: 396px;
    width: 732px; height: 429px;
    background: var(--card);
    border-radius: 22px;
    box-shadow: 0 6px 18px rgba(0,0,0,0.18);
    font-family: "Montserrat", sans-serif;
  }
  .title-band {
    position: absolute; left: 30px; right: 30px; top: 42px; height: 60px;
    background: var(--band);
    border-radius: 8px;
    display: flex; align-items: center; justify-content: center;
  }
  .title-band h1 {
    font-family: "Archivo Black", sans-serif;
    color: var(--band-text);
    font-size: 30px; letter-spacing: 0.4px;
    font-weight: 400; white-space: nowrap;
  }
  .speaking-art {
    position: absolute; left: 36px; top: 144px;
    width: 360px; height: 264px;
    border-radius: 14px;
    background: linear-gradient(135deg, var(--art-a), var(--art-b));
  }
  .contact {
    position: absolute; right: 30px; top: 162px; width: 300px;
    text-align: right;
  }
  .contact .name {
    color: var(--name); font-weight: 700; font-size: 22px; letter-spacing: 0.6px;
  }
  .contact .credentials {
    color: var(--name); font-size: 14px; font-weight: 400; margin-top: 4px;
  }
  .contact-line {
    display: flex; align-items: center; justify-content: flex-end; gap: 10px;
    margin-top: 8px; font-size: 15px;
  }
  .contact-line.phone { margin-top: 16px; color: var(--email); }
  .contact-line.email { color: var(--email); }
  .contact-line svg { width: 20px; height: 20px; flex: none; }
  .association {
    position: absolute; left: 507px; top: 354px;
    display: flex; align-items: center; gap: 12px;
  }
  .association .dot {
    width: 44px; height: 44px; border-radius: 50%; background: var(--mark);
  }
  .association span {
    font-weight: 700; font-size: 24px; color: var(--mark); letter-spacing: 1px;
  }
</style>
</head>
<body>
  <main class="business-card">
    <header class="title-band"><h1>SPEECH-LANGUAGE PATHOLOGIST</h1></header>

    <div class="speaking-art" role="img" aria-label="Cartoon child shouting into a megaphone with sound lines"></div>

    <section class="contact">
      <p class="name">ROSALIND PETTRY</p>
      <p class="credentials">M.S. CCC-SLP/TSSLD</p>
      <p class="contact-line phone">415 906 2283
        <svg viewBox="0 0 20 20" aria-hidden="true"><circle cx="10" cy="10" r="10" fill="var(--icon)"/><path d="M7 5.5l1.6 2.2-1 1.1a6 6 0 0 0 3.4 3.4l1.1-1 2.2 1.6-.8 1.6c-3.8.2-7.5-3.5-7.3-7.3z" fill="#fff"/></svg>
      </p>
      <p class="contact-line email">rosiepettry@kelvormail.net
        <svg viewBox="0 0 20 20" aria-hidden="true"><circle cx="10" cy="10" r="10" fill="var(--icon)"/><rect x="5" y="6.5" width="10" height="7" rx="1" fill="#fff"/><path d="M5.5 7l4.5 3.5L14.5 7" fill="none" stroke="var(--icon)" stroke-width="1.2"/></svg>
      </p>
    </section>

    <div class="association"><div class="dot"></div><span>KROV</span></div>
  </main>
</body>
</html>
```